Business cards and logo for a international shipping company called Harborline Freight LLC. We would like to incorporate the colors red and blue. We would like the theme to be nautical.

Industry/Entity Type

Business

```html
<!DOCTYPE html>
<html lang="en">
<head>
<meta charset="utf-8">
<title>Harborline Freight LLC – Business Card</title>
<link href="https://fonts.googleapis.com/css2?family=Cinzel:wght@700&family=Raleway:wght@400&family=Roboto+Condensed:ital,wght@0,400;1,700&display=swap" rel="stylesheet">
<style>
  :root {
    --stage: #3a3a3a;
    --teal: #17a6b6;
    --teal-deep: #0f9aab;
    --teal-ink: #1aa0ad;
    --red: #c02026;
    --red-text: #e04a2f;
    --white: #ffffff;
    --ink: #2b2b2b;
    --grey: #4a4a4a;
  }
  * { margin: 0; padding: 0; box-sizing: border-box; }
  html, body { width: 1200px; height: 1200px; overflow: hidden; }
  body { background: var(--stage); position: relative; }

  .card {
    position: absolute;
    left: 194px;
    width: 839px;
    height: 476px;
    overflow: hidden;
  }
  .card--front { top: 84px; background: linear-gradient(180deg, var(--teal) 0%, var(--teal-deep) 100%); }
  .card--back { top: 654px; background: var(--white); }

  .corner-stripes { position: absolute; inset: 0; width: 839px; height: 476px; }

  /* front */
  .front-title {
    position: absolute; top: 52px; left: 0; width: 100%;
    text-align: center;
    font-family: "Cinzel", serif; font-weight: 700;
    font-size: 44px; color: var(--white); letter-spacing: 0.5px;
  }
  .front-art {
    position: absolute; left: 0; top: 120px; width: 430px; height: 330px;
    background: radial-gradient(ellipse at 55% 45%, #e8f3f5 0%, #9fd0d8 45%, rgba(23,166,182,0) 75%);
  }
  .front-tagline {
    position: absolute; left: 410px; top: 200px;
    font-family: "Raleway", sans-serif; font-weight: 400;
    font-size: 26px; line-height: 32px; color: var(--ink);
  }

  /* back */
  .back-wave {
    position: absolute; left: 0; top: 40px; width: 520px; height: 300px;
    background: radial-gradient(ellipse at 10% 40%, #dfe8f5 0%, rgba(255,255,255,0) 65%);
  }
  .back-art {
    position: absolute; left: 446px; top: 138px; width: 368px; height: 330px;
    background: radial-gradient(ellipse at 55% 60%, #c9dbe6 0%, #e6eef3 45%, rgba(255,255,255,0) 75%);
  }
  .back-title {
    position: absolute; top: 52px; left: 0; width: 100%;
    text-align: center;
    font-family: "Cinzel", serif; font-weight: 700;
    font-size: 44px; line-height: 48px; color: var(--teal-ink);
  }
  .back-tagline {
    position: absolute; top: 102px; left: 0; width: 100%;
    text-align: center;
    font-family: "Raleway", sans-serif; font-weight: 400;
    font-size: 24px; color: var(--grey);
  }
  .person { position: absolute; left: 93px; top: 186px; font-family: "Roboto Condensed", sans-serif; }
  .person-name { font-style: italic; font-weight: 700; font-size: 38px; line-height: 42px; color: var(--red-text); }
  .person-role { font-size: 22px; color: var(--grey); margin-top: 4px; }

  .contacts { position: absolute; left: 93px; top: 280px; list-style: none; font-family: "Roboto Condensed", sans-serif; }
  .contact { display: flex; align-items: center; height: 40px; font-size: 22px; color: #222; }
  .contact-icon { width: 22px; height: 22px; margin-right: 14px; color: var(--red-text); display: flex; align-items: center; justify-content: center; font-size: 24px; font-style: italic; }
  .toll-free {
    position: absolute; left: 93px; top: 402px;
    font-family: "Roboto Condensed", sans-serif; font-style: italic; font-weight: 700;
    font-size: 29px; color: var(--teal-ink);
  }
</style>
</head>
<body>

<section class="card card--front">
  <div class="front-art" role="img" aria-label="Illustration of a cargo plane over a container ship, a globe with parcels and delivery vans"></div>
  <h1 class="front-title">HARBORLINE FREIGHT LLC</h1>
  <p class="front-tagline">INTERNATIONAL<br>SHIPPING<br>COMPANY</p>
  <svg class="corner-stripes" viewBox="0 0 839 476" aria-hidden="true">
    <polygon points="839,105 542,402 585,402 839,148" fill="var(--white)"/>
    <polygon points="839,148 511,476 839,476" fill="var(--red)"/>
  </svg>
</section>

<section class="card card--back">
  <div class="back-wave" role="img" aria-label="Soft pale blue flowing wave lines"></div>
  <div class="back-art" role="img" aria-label="Illustration of a cargo plane, container ship, globe with parcels and delivery vans"></div>
  <h2 class="back-title">HARBORLINE FREIGHT LLC</h2>
  <p class="back-tagline">INTERNATIONAL SHIPPING COMPANY</p>

  <div class="person">
    <p class="person-name">Daniel Reyes</p>
    <p class="person-role">Founder/Director</p>
  </div>

  <ul class="contacts">
    <li class="contact">
      <span class="contact-icon">
        <svg viewBox="0 0 24 24" width="20" height="22"><path d="M7 2c1 0 2 3 2.5 4.5.3 1-1.5 2-1.5 3 0 2 3 6.5 5 7.5 1 .5 2-1.3 3-1 1.5.5 4 1.5 4 2.5 0 1.5-2 3.5-4 3.5C9 22 2 12 2 7c0-2 3-5 5-5z" fill="currentColor"/></svg>
      </span>615.555.0142
    </li>
    <li class="contact"><span class="contact-icon">@</span>harborlinefreight@mailbox.com</li>
    <li class="contact">
      <span class="contact-icon">
        <svg viewBox="0 0 24 24" width="22" height="22" fill="none" stroke="currentColor" stroke-width="1.6"><circle cx="12" cy="12" r="10"/><ellipse cx="12" cy="12" rx="4.5" ry="10"/><line x1="2" y1="12" x2="22" y2="12"/><path d="M4 7h16M4 17h16"/></svg>
      </span>harborlinefreightllc.com
    </li>
  </ul>

  <p class="toll-free">Toll Free: 888-555-0174</p>

  <svg class="corner-stripes" viewBox="0 0 839 476" aria-hidden="true">
    <polygon points="839,318 750,407 795,407 839,363" fill="var(--white)"/>
    <polygon points="839,363 726,476 839,476" fill="var(--red)"/>
  </svg>
</section>

</body>
</html>
```